Elegant and Professional Business card design needed

The client journey mentor is a company which provides consulting services to businesses to assist them in improving the customer experience for their customers.

I need a business card design which tells people I'm there to help them.

Target Market(s)

Small to medium business owners

Industry/Entity Type

Business

Contact Information for Business Card

Leonard Pashcroft
The Client Journey Mentor
Web: http://www.TheClientJourneyMentor.example
Email: leonard@TheClientJourneyMentor.example
Phone: +61 452 386017

Logo styles of interest
Abstract Logo
Requirements
Must have
• Some sort of image / graphic representing the customer is important and should be at the heart of a business.

```html
<!DOCTYPE html>
<html lang="en">
<head>
<meta charset="utf-8">
<title>The Client Journey Mentor – Business Cards</title>
<link href="https://fonts.googleapis.com/css2?family=Open+Sans:wght@400;700&family=Montserrat:wght@500;600&display=swap" rel="stylesheet">
<style>
:root{
  --canvas:#eceeef;
  --white:#ffffff;
  --red:#d63b34;
  --red-dark:#b52a24;
  --orange:#d9772e;
  --orange-dark:#c2611d;
  --yellow:#cbc52c;
  --yellow-dark:#b3a91c;
  --green:#93c43c;
  --green-dark:#5f9e2e;
  --ink:#2b2b2b;
  --ink-soft:#3a3a3a;
  --sky:#9cc3e3;
}
*{margin:0;padding:0;box-sizing:border-box}
html,body{width:950px;height:1200px;overflow:hidden;background:var(--canvas)}
.canvas{position:relative;width:950px;height:1200px}

/* Front card */
.card-front{position:absolute;left:74px;top:77px;width:814px;height:468px;background:var(--white);border-radius:22px;overflow:hidden;box-shadow:0 2px 8px rgba(0,0,0,.18);font-family:'Open Sans',Arial,sans-serif}
.front-band{position:absolute;left:0;right:0;top:275px;bottom:0;background:linear-gradient(90deg,var(--green) 0%,#8fc23a 60%,var(--green-dark) 100%)}
.service-tile{position:absolute;top:43px;width:164px;height:232px;border-radius:10px 10px 0 0;color:var(--white);text-align:center;box-shadow:0 1px 3px rgba(0,0,0,.25)}
.service-tile.strategy{left:68px;background:linear-gradient(180deg,#e9584f,var(--red-dark))}
.service-tile.design{left:240px;background:linear-gradient(180deg,#eb8c43,var(--orange-dark))}
.service-tile.insight{left:410px;background:linear-gradient(180deg,#dcd743,var(--yellow-dark))}
.service-tile.plan{left:582px;background:linear-gradient(180deg,#a6d25a,#78b03a)}
.tile-photo{position:absolute;left:27px;top:21px;width:110px;height:110px;border-radius:50%;border:4px solid var(--white);background:radial-gradient(circle at 40% 40%,#ffffff,#d6dbe0)}
.tile-label{position:absolute;left:0;right:0;top:138px;font-weight:700;font-size:21px;line-height:22px;text-shadow:0 1px 2px rgba(0,0,0,.35)}
.brand-pill{position:absolute;left:140px;top:269px;width:521px;height:37px;background:var(--white);border-radius:6px;color:var(--red);font-weight:700;font-size:23px;line-height:37px;text-align:center;text-transform:uppercase}
.front-contact{position:absolute;left:0;right:0;top:316px;text-align:center}
.front-name{color:var(--white);font-weight:700;font-size:23px;text-transform:uppercase;text-shadow:0 1px 2px rgba(0,0,0,.3)}
.front-phone{color:var(--white);font-weight:700;font-size:27px;margin-top:2px;text-shadow:0 1px 2px rgba(0,0,0,.3)}
.front-phone svg{width:20px;height:20px;vertical-align:-1px;margin-right:2px}
.front-line{color:var(--ink-soft);font-size:19px;line-height:26px}
.front-line svg{width:18px;height:14px;vertical-align:-1px;margin-right:8px}

/* Back card */
.card-back{position:absolute;left:64px;top:647px;width:821px;height:474px;box-shadow:0 2px 8px rgba(0,0,0,.18);background:var(--white)}
.card-back svg{display:block}
.back-title{font-family:'Montserrat','Century Gothic',sans-serif;font-weight:600;font-size:27px;fill:var(--white)}
.back-name{font-family:'Montserrat','Century Gothic',sans-serif;font-weight:600;font-size:27px;fill:var(--ink)}
.back-phone{font-family:'Montserrat','Century Gothic',sans-serif;font-weight:600;font-size:24px;fill:var(--red)}
.back-line{font-family:'Montserrat','Century Gothic',sans-serif;font-weight:500;font-size:19px;fill:var(--ink-soft)}
</style>
</head>
<body>
<div class="canvas">

  <section class="card-front">
    <div class="front-band"></div>
    <div class="service-tile strategy"><div class="tile-photo" role="img" aria-label="Photo of a hand sketching a strategy diagram"></div><div class="tile-label">Customer<br>Strategy</div></div>
    <div class="service-tile design"><div class="tile-photo" role="img" aria-label="Photo of a customer journey map document"></div><div class="tile-label">Customer<br>Experience<br>Design</div></div>
    <div class="service-tile insight"><div class="tile-photo" role="img" aria-label="Photo of a clock reading time for feedback"></div><div class="tile-label">Customer<br>Insight</div></div>
    <div class="service-tile plan"><div class="tile-photo" role="img" aria-label="Photo of hands writing on a notepad"></div><div class="tile-label">Customer<br>Improvement<br>Plan</div></div>
    <div class="brand-pill">The Client Journey Mentor</div>
    <div class="front-contact">
      <div class="front-name">Leonard Pashcroft</div>
      <div class="front-phone"><svg viewBox="0 0 24 24"><path fill="#fff" d="M6.6 10.8a15 15 0 0 0 6.6 6.6l2.2-2.2c.3-.3.7-.4 1-.2 1.1.4 2.3.6 3.6.6.6 0 1 .4 1 1V20c0 .6-.4 1-1 1A17 17 0 0 1 3 4c0-.6.4-1 1-1h3.5c.6 0 1 .4 1 1 0 1.3.2 2.5.6 3.6.1.3 0 .7-.2 1z"/></svg>+61 452 386017</div>
      <div class="front-line"><svg viewBox="0 0 18 14"><rect x="1" y="1" width="16" height="12" fill="none" stroke="#3a3a3a" stroke-width="1.4"/><path d="M1 1l8 7 8-7" fill="none" stroke="#3a3a3a" stroke-width="1.4"/></svg>leonard@TheClientJourneyMentor.example</div>
      <div class="front-line"><svg viewBox="0 0 18 14"><circle cx="9" cy="7" r="6" fill="none" stroke="#3a3a3a" stroke-width="1.3"/><ellipse cx="9" cy="7" rx="2.6" ry="6" fill="none" stroke="#3a3a3a" stroke-width="1.1"/><path d="M3 7h12" stroke="#3a3a3a" stroke-width="1.1"/></svg>www.TheClientJourneyMentor.example</div>
    </div>
  </section>

  <section class="card-back">
    <svg width="821" height="474" viewBox="0 0 821 474">
      <defs>
        <linearGradient id="back-green" x1="0" x2="1" y1="0" y2="0"><stop offset="0" stop-color="#9cc93b"/><stop offset="1" stop-color="#64a232"/></linearGradient>
        <linearGradient id="back-orange" x1="0" x2="1"><stop offset="0" stop-color="#d9772e"/><stop offset="1" stop-color="#cf6d28"/></linearGradient>
        <linearGradient id="sky-top" x1="0" y1="0" x2="0" y2="1"><stop offset="0" stop-color="#5f93c9"/><stop offset="1" stop-color="#dfe9f3"/></linearGradient>
        <linearGradient id="sky-bottom" x1="0" y1="0" x2="0" y2="1"><stop offset="0" stop-color="#3f7fc2"/><stop offset="1" stop-color="#b8d3ec"/></linearGradient>
      </defs>
      <polygon points="239,0 821,0 821,86 239,206" fill="url(#back-orange)"/>
      <polygon points="239,436 821,306 821,474 239,474" fill="url(#back-green)"/>
      <polygon points="239,431 821,301 821,309 239,439" fill="var(--red)"/>
      <rect x="0" y="0" width="239" height="242" fill="url(#sky-top)" role="img" aria-label="Photo of businessmen climbing a rising red graph against the sky"/>
      <rect x="0" y="242" width="239" height="232" fill="url(#sky-bottom)" role="img" aria-label="Photo of a businessman aiming a bow at a cloud target"/>

      <text class="back-title" x="250" y="183" transform="rotate(-11.5 250 183)">The Client Journey Mentor</text>
      <text class="back-name" x="372" y="236" transform="rotate(-11.5 372 236)">Leonard Pashcroft</text>
      <g transform="rotate(-11.5 411 283)">
        <path transform="translate(384 264) scale(.85)" fill="var(--red)" d="M6.6 10.8a15 15 0 0 0 6.6 6.6l2.2-2.2c.3-.3.7-.4 1-.2 1.1.4 2.3.6 3.6.6.6 0 1 .4 1 1V20c0 .6-.4 1-1 1A17 17 0 0 1 3 4c0-.6.4-1 1-1h3.5c.6 0 1 .4 1 1 0 1.3.2 2.5.6 3.6.1.3 0 .7-.2 1z"/>
        <text class="back-phone" x="411" y="283">+61 452 386017</text>
      </g>
      <g transform="rotate(-11.5 314 350)">
        <rect x="287" y="336" width="18" height="13" fill="none" stroke="#3a3a3a" stroke-width="1.4"/>
        <path d="M287 336l9 7 9-7" fill="none" stroke="#3a3a3a" stroke-width="1.4"/>
        <text class="back-line" x="314" y="350">leonard@TheClientJourneyMentor.example</text>
      </g>
      <g transform="rotate(-11.5 314 378)">
        <circle cx="296" cy="371" r="7" fill="none" stroke="#3a3a3a" stroke-width="1.3"/>
        <ellipse cx="296" cy="371" rx="3" ry="7" fill="none" stroke="#3a3a3a" stroke-width="1.1"/>
        <path d="M289 371h14" stroke="#3a3a3a" stroke-width="1.1"/>
        <text class="back-line" x="314" y="378">www.TheClientJourneyMentor.example</text>
      </g>
    </svg>
  </section>

</div>
</body>
</html>
```